Commercial Property Management Company needs business card design

We need an elegant business card design for our commercial property management company based in Hampton Falls, New Hampshire. We manage large retail shopping centers. These cards will be going out to current clients, retailers and to contractors.
I am the sole member of the company, so I'm not sure if I need to have a title with my name or not.

Industry/Entity Type

Property Management

Contact Information for Business Card

Dalton R. Pike
4 Kestler Lane
Alder Falls, NH 03871
Cell: (603) 555-0148
Fax: (603) 555-0172
Email: dalton@korvelmanagementllc.com

```html
<!DOCTYPE html>
<html lang="en">
<head>
<meta charset="utf-8">
<title>Korvel Management, LLC — Business Card</title>
<link rel="stylesheet" href="https://fonts.googleapis.com/css2?family=Jost:wght@400;500;600&display=swap">
<style>
  :root {
    --backdrop: #e3e7ed;
    --card-brown: #7b5c45;
    --card-white: #f7f7f5;
    --name-silver: #ece6df;
    --ink: #2b2b2b;
    --rule: #c9c9c9;
    --mark-red: #a3341d;
    --shadow: rgba(40, 50, 70, 0.22);
  }
  * { box-sizing: border-box; margin: 0; padding: 0; }
  html, body {
    width: 1200px; height: 1000px; overflow: hidden;
    background: var(--backdrop);
    font-family: "Jost", sans-serif;
  }
  .canvas {
    width: 1200px; height: 1000px;
    display: flex; flex-direction: column;
    align-items: center; justify-content: center; gap: 70px;
  }
  .card {
    position: relative;
    width: 580px; height: 332px;
    border-radius: 4px;
    box-shadow: 0 14px 30px var(--shadow);
  }
  /* Front */
  .card-front { background: var(--card-brown); }
  .front-brand {
    position: absolute; left: 0; right: 0; top: 92px;
    display: flex; flex-direction: column; align-items: center;
  }
  .front-mark {
    width: 64px; height: 64px; border-radius: 50%;
    background: var(--mark-red); margin-bottom: 18px;
  }
  .front-name {
    font-size: 30px; font-weight: 400; letter-spacing: 1px;
    color: var(--name-silver);
  }
  .front-tagline {
    margin-top: 4px; font-size: 14px; letter-spacing: 1.2px;
    color: var(--name-silver);
  }
  /* Back */
  .card-back { background: var(--card-white); color: var(--ink); }
  .back-brand {
    position: absolute; right: 62px; top: 34px;
    display: flex; flex-direction: column; align-items: center;
  }
  .back-mark {
    width: 80px; height: 80px; border-radius: 50%;
    background: var(--mark-red);
  }
  .back-brand-name {
    margin-top: 8px; font-size: 11px; font-weight: 500;
    letter-spacing: 1px; color: var(--ink);
  }
  .divider {
    position: absolute; left: 250px; right: 36px; top: 160px;
    height: 1px; background: var(--rule);
  }
  .person {
    position: absolute; left: 40px; top: 196px;
  }
  .person-name {
    font-size: 19px; font-weight: 600; letter-spacing: 2.6px;
    text-transform: uppercase; margin-bottom: 12px;
  }
  .contact-line { font-size: 14px; line-height: 1.4; }
  .office {
    position: absolute; left: 322px; top: 174px;
  }
  .office-name {
    font-size: 12px; font-weight: 600; letter-spacing: 1px;
    text-transform: uppercase; margin-bottom: 3px;
  }
  .office-line { font-size: 13px; line-height: 1.35; }
</style>
</head>
<body>
<main class="canvas">
  <section class="card card-front" aria-label="Business card front">
    <div class="front-brand">
      <div class="front-mark"></div>
      <p class="front-name">Korvel Management, LLC</p>
      <p class="front-tagline">Commercial property management</p>
    </div>
  </section>

  <section class="card card-back" aria-label="Business card back">
    <div class="back-brand">
      <div class="back-mark"></div>
      <p class="back-brand-name">Korvel Management</p>
    </div>
    <div class="divider"></div>
    <div class="person">
      <h1 class="person-name">Dalton R. Pike</h1>
      <p class="contact-line">Cell: (603) 555-0148</p>
      <p class="contact-line">Fax: (603) 555-0172</p>
      <p class="contact-line">dalton@korvelmanagementllc.com</p>
    </div>
    <div class="office">
      <p class="office-name">Korvel Management</p>
      <p class="office-line">4 Kestler Lane</p>
      <p class="office-line">Alder Falls, NH 03871</p>
    </div>
  </section>
</main>
</body>
</html>
```